Equestrian brand 'health check' webinar template

I am looking to host a series of webinars promoting my consulting business in equestrian business development. I work mainly with start-ups and young brands looking to establish their brand in the international equestrian marketplace mainly focussed on horse riding fashion and horse riding essentials.
The topic of the webinar is a 'brand health check': helping brands understand what they really stand for if they are really 'talking' to the right audience and delivering the right message. Additionally, we'll touch on having all the brand fundamentals in place to become successful.
I am looking for a webinar/presentation template that is professional and shows off the topics in the best possible way, in keeping with the equestrian theme and the current look and feel of the website: thecopperlanternadvisorygroup.com
Target Market(s)
Equestrian businesses, start-up, fashion
Industry/Entity Type
Business
Logo Text
conceptual high market equestrian services style
Colors

```html
<!DOCTYPE html>
<html lang="en">
<head>
<meta charset="utf-8">
<title>The Copper Lantern Advisory Group – Webinar Template</title>
<link rel="stylesheet" href="https://fonts.googleapis.com/css2?family=Jost:wght@300;400&family=Great+Vibes&display=swap">
<style>
  :root {
    --page-bg: #a8a8a8;
    --plum-deep: #220f21;
    --plum-mid: #4a2546;
    --plum-light: #a174a3;
    --ink-band: rgba(24, 22, 24, 0.9);
    --white: #ffffff;
    --text-soft: #e9dde8;
    --photo-dark: #3c3c3c;
    --photo-mid: #8a8a8a;
    --photo-light: #d9d9d9;
  }
  * { margin: 0; padding: 0; box-sizing: border-box; }
  html, body { width: 1200px; height: 2616px; overflow: hidden; }
  body {
    background: var(--page-bg);
    position: relative;
    font-family: "Jost", "Helvetica Neue", Arial, sans-serif;
    font-weight: 300;
    color: var(--white);
  }
  .slide {
    position: absolute;
    left: 119px;
    width: 942px;
    height: 530px;
    overflow: hidden;
  }
  .slide--cover { top: 77px; }
  .slide--welcome { top: 699px; }
  .slide--services { top: 1322px; }
  .slide--closing { top: 1948px; }

  .photo { position: absolute; top: 0; left: 0; height: 100%; }
  .photo--cover {
    width: 100%;
    background: linear-gradient(100deg, var(--photo-mid) 0%, var(--photo-light) 35%, var(--photo-dark) 60%, var(--photo-mid) 100%);
  }
  .photo--welcome {
    width: 413px;
    background: linear-gradient(160deg, var(--photo-light) 0%, var(--photo-mid) 30%, var(--photo-dark) 60%, var(--photo-mid) 100%);
  }
  .photo--services {
    width: 413px;
    background: linear-gradient(170deg, var(--photo-dark) 0%, #6e6e6e 45%, var(--photo-mid) 75%, #b5b5b5 100%);
  }
  .photo--closing {
    width: 100%;
    background: linear-gradient(180deg, var(--plum-deep) 0%, var(--plum-mid) 40%, #6a4468 65%, var(--plum-mid) 100%);
  }

  .panel-right {
    position: absolute; top: 0; right: 0;
    width: 529px; height: 100%;
    background: linear-gradient(200deg, var(--plum-deep) 0%, var(--plum-mid) 55%, var(--plum-light) 120%);
  }

  .frame {
    position: absolute;
    top: 17px; left: 17px; right: 17px; bottom: 17px;
    border: 1.5px solid rgba(255,255,255,0.85);
    pointer-events: none;
  }

  .cover-panel { position: absolute; inset: 0; }
  .cover-title {
    position: absolute; right: 28px; top: 216px;
    text-align: right; font-size: 24px; font-weight: 400;
    line-height: 1.25; letter-spacing: 0.5px; text-transform: uppercase;
  }
  .cover-subtitle {
    position: absolute; right: 28px; top: 296px;
    font-size: 15px; font-weight: 300; text-transform: uppercase; letter-spacing: 0.3px;
  }

  .content { position: absolute; left: 452px; right: 42px; }
  .welcome-heading {
    top: 42px; font-size: 40px; font-weight: 300; letter-spacing: 1px;
  }
  .welcome-rule {
    position: absolute; left: 452px; top: 100px; width: 218px; height: 2px; background: var(--white);
  }
  .pillars {
    position: absolute; left: 448px; right: 36px; top: 134px;
    display: flex; justify-content: space-between;
  }
  .pillar { width: 120px; text-align: center; }
  .pillar svg { display: block; margin: 0 auto 14px; }
  .pillar-label { font-size: 14px; text-transform: uppercase; }
  .pillar:first-child { text-align: left; }
  .pillar:first-child svg { margin-left: 8px; }
  .pillar:last-child { text-align: right; }
  .pillar:last-child svg { margin-right: 22px; margin-left: auto; }

  .body-copy { font-size: 11.6px; line-height: 1.4; color: var(--text-soft); }
  .body-copy p + p { margin-top: 12px; }
  .welcome-copy { top: 262px; }

  .services { left: 445px; top: 26px; right: 42px; }
  .section-heading { font-size: 21px; font-weight: 300; text-transform: uppercase; margin-bottom: 6px; }
  .services .body-copy { margin-bottom: 22px; }
  .brand-list { list-style: none; font-size: 11.6px; line-height: 1.5; color: var(--text-soft); margin-bottom: 18px; }
  .brand-list li::before { content: "•"; margin-right: 12px; }
  .riders-line { font-size: 11.6px; color: var(--text-soft); }

  .closing-logo {
    position: absolute; left: 0; right: 0; top: 62px; text-align: center;
    font-size: 58px; font-weight: 400; line-height: 1;
  }
  .closing-logo small { display: block; font-size: 20px; margin-top: 2px; margin-left: 30px; }
  .closing-thanks {
    position: absolute; left: 0; right: 0; top: 240px; text-align: center;
    font-family: "Great Vibes", cursive; font-size: 86px; line-height: 1;
  }
  .closing-url {
    position: absolute; left: 0; right: 0; bottom: 44px; text-align: center;
    font-size: 22px; font-weight: 400;
  }
</style>
</head>
<body>

<section class="slide slide--cover">
  <div class="photo photo--cover" role="img" aria-label="Black and white photo of a smiling young woman stroking a horse's face by a paddock fence"></div>
  <svg class="cover-panel" width="942" height="530" viewBox="0 0 942 530" aria-hidden="true">
    <defs>
      <linearGradient id="cover-plum" x1="1" y1="0" x2="0" y2="1">
        <stop offset="0" stop-color="#220f21"/>
        <stop offset="0.55" stop-color="#4a2546"/>
        <stop offset="1" stop-color="#a174a3"/>
      </linearGradient>
    </defs>
    <polygon points="623,0 942,0 942,530 457,530" fill="url(#cover-plum)"/>
    <rect x="513" y="208" width="429" height="116" fill="rgba(24,22,24,0.9)"/>
    <rect x="17" y="17" width="908" height="496" fill="none" stroke="rgba(255,255,255,0.85)" stroke-width="1.5"/>
  </svg>
  <h1 class="cover-title">The Copper Lantern<br>Advisory Group</h1>
  <p class="cover-subtitle">Equestrian Business Development</p>
</section>

<section class="slide slide--welcome">
  <div class="photo photo--welcome" role="img" aria-label="Black and white photo of a woman greeting a dark horse in a field"></div>
  <div class="panel-right"></div>
  <div class="frame"></div>
  <h2 class="content welcome-heading">WELCOME</h2>
  <div class="welcome-rule"></div>
  <div class="pillars">
    <div class="pillar">
      <svg width="60" height="60" viewBox="0 0 60 60" aria-hidden="true">
        <circle cx="30" cy="30" r="28" fill="#d8d8d8" stroke="#fff" stroke-width="2"/>
        <circle cx="30" cy="30" r="22" fill="#bdbdbd"/>
        <circle cx="30" cy="23" r="5" fill="#333"/>
        <path d="M21 40c0-7 4-10 9-10s9 3 9 10z" fill="#333"/>
        <circle cx="20" cy="26" r="3.5" fill="#555"/>
        <path d="M14 39c0-5 3-8 6-8s4 2 4 2l-2 6z" fill="#555"/>
        <circle cx="40" cy="26" r="3.5" fill="#555"/>
        <path d="M46 39c0-5-3-8-6-8s-4 2-4 2l2 6z" fill="#555"/>
      </svg>
      <span class="pillar-label">Personal</span>
    </div>
    <div class="pillar">
      <svg width="60" height="60" viewBox="0 0 60 60" aria-hidden="true">
        <circle cx="30" cy="30" r="28" fill="#d8d8d8" stroke="#fff" stroke-width="2"/>
        <circle cx="30" cy="30" r="22" fill="#bdbdbd"/>
        <circle cx="30" cy="23" r="7" fill="#333"/>
        <path d="M17 44c0-9 6-13 13-13s13 4 13 13z" fill="#333"/>
        <path d="M28 32l2 8 2-8z" fill="#bdbdbd"/>
      </svg>
      <span class="pillar-label">Professional</span>
    </div>
    <div class="pillar">
      <svg width="60" height="60" viewBox="0 0 60 60" aria-hidden="true">
        <circle cx="30" cy="30" r="28" fill="#d8d8d8" stroke="#fff" stroke-width="2"/>
        <circle cx="30" cy="30" r="22" fill="#bdbdbd"/>
        <rect x="19" y="36" width="4" height="7" fill="#333"/>
        <rect x="25" y="32" width="4" height="11" fill="#333"/>
        <rect x="31" y="28" width="4" height="15" fill="#333"/>
        <rect x="37" y="24" width="4" height="19" fill="#333"/>
        <path d="M18 30l9-7 6 4 9-9" fill="none" stroke="#333" stroke-width="2"/>
        <path d="M38 17h5v5z" fill="#333"/>
      </svg>
      <span class="pillar-label">Performance</span>
    </div>
  </div>
  <div class="content welcome-copy body-copy">
    <p>Getting you one stride ahead in the world of equestrian business development, Go-to-market strategy, product development, branding, social media, and marketing. Whether you're an equestrian business, an accomplished rider or an equestrian social media influencer, The Copper Lantern Advisory Group can help you get your business to Grand-Prix level with a variety of tailored support packages.</p>
    <p>Whether it's long-distance business coaching calls, full day marketing strategy workshops or product database development and pricing strategy, we will always have a solution to help you jump higher, piaff stronger and improve your overall performance and achieve your business goals.</p>
    <p>Get in touch for a FREE 30 min call to understand how we can help your business in the best possible way.</p>
  </div>
</section>

<section class="slide slide--services">
  <div class="photo photo--services" role="img" aria-label="Black and white photo of a horse's legs in protective boots cantering in a sand arena"></div>
  <div class="panel-right"></div>
  <div class="frame"></div>
  <div class="content services">
    <h2 class="section-heading">Services</h2>
    <div class="body-copy">
      <p>The Copper Lantern Advisory Group aims to help you focus on what you do best, whether that is starting up your equestrian business, training horses, developing your equestrian style or sourcing the best products for your tack shop, chances are, you might not have time or the expertise to work on your business development strategy, personal branding, or social media presence to attract sponsors.</p>
      <p>This is where The Copper Lantern Advisory Group can help you with a personal tailor-made touch. With an established network in marketing, services and the equestrian industry, we all always be able to find the best solution to suit your needs. Get in touch to see what an independent Free Lance general manager for hire can do for your business!</p>
    </div>
    <h2 class="section-heading">Brands</h2>
    <ul class="brand-list">
      <li>Business development</li>
      <li>Branding</li>
      <li>(Retail) Marketing strategy</li>
      <li>Social media strategy</li>
      <li>Go-to-Market strategy</li>
      <li>Product development, product selection, collection strategy</li>
      <li>Market (re)positioning (price, image, design)</li>
      <li>Long-term strategic international sales strategy</li>
    </ul>
    <h2 class="section-heading">Riders</h2>
    <p class="riders-line">Personal PR | Sponsor opportunities | Network Business development strategy</p>
  </div>
</section>

<section class="slide slide--closing">
  <div class="photo photo--closing" role="img" aria-label="Purple-toned close-up of a horse's neck with a row of braided mane knots"></div>
  <div class="frame"></div>
  <p class="closing-logo">LOGO<small>here</small></p>
  <p class="closing-thanks">Thank You</p>
  <p class="closing-url">www.thecopperlanternadvisorygroup.com</p>
</section>

</body>
</html>
```